Clinic for cellulit and fat removal

Name of clinic :
Velmora
- Body & Health (this has to be written on the site.)
I need CMS for me to be able to make changes myself.
A webpage for woman searching for a solution to remove fat and cellulit.
The owner is a brazilian woman in Denmark, and want her sense of aestetic shines thru the website.
There needs to be a slide show on the landing page showing big sliding pictures, of the clinic and and the treatments.
The Cryolipolysis, is a treatment freezing fat and cellulit, and this treatment will be the Attraction of the clinic.
Needs These pages in a horisontal fasion. (written in Danish)
Velmora
Behandlinger
- Cryolipolysis
- Trimcurve
- Lymfemassage
- Restalogic
- Radiant Pulse
Produkter
Priser
Kontakt
Clinic

```html
<!DOCTYPE html>
<html lang="da">
<head>
<meta charset="utf-8">
<title>Velmora – Body &amp; Health</title>
<link href="https://fonts.googleapis.com/css2?family=Jost:wght@300;400;500&family=Open+Sans:wght@400;600&display=swap" rel="stylesheet">
<style>
:root{
  --teal:#8ccfb9;
  --teal-light:#d7efe7;
  --nav:#2b2b2b;
  --nav-line:#3d3d3d;
  --magenta:#a51c7a;
  --date:#c0166f;
  --ink:#222;
  --text:#555;
  --grey-bg:#f2f2f2;
  --footer-bg:#f4f4f4;
  --white:#fff;
  --green-link:#6cae3c;
  --skin:#e9c3aa;
  --skin-deep:#c98f6e;
  --steel:#9aa4ad;
  --glove:#5b6fb8;
}
*{box-sizing:border-box;margin:0;padding:0}
html,body{width:1200px;height:2817px;overflow:hidden}
body{background:var(--white);font-family:"Open Sans",Arial,sans-serif;color:var(--text);position:relative}
.heading{font-family:"Jost",Arial,sans-serif;font-weight:400;color:var(--ink)}

/* header */
.site-header{position:absolute;top:0;left:0;width:1200px;height:131px}
.brand{position:absolute;left:98px;top:22px;display:flex;align-items:center;gap:14px}
.brand-dot{width:22px;height:22px;border-radius:50%;background:var(--teal)}
.brand-text{font-family:"Jost",sans-serif;font-weight:400;color:var(--ink);line-height:1}
.brand-name{font-size:44px;display:block}
.brand-tag{font-size:16px;display:block;margin-top:6px;letter-spacing:.5px}
.search{position:absolute;left:727px;top:45px;width:231px;height:36px;border:1px solid #bbb;border-radius:3px;font-size:11px;color:#333;padding:10px 10px}
.search svg{position:absolute;right:10px;top:11px}
.lang{position:absolute;left:992px;top:56px;font-size:15px;color:#555}
.lang .active{color:var(--green-link)}

.main-nav{position:absolute;top:131px;left:0;width:1200px;height:51px;background:var(--nav);display:flex;padding-left:100px}
.main-nav a{display:block;height:51px;line-height:51px;padding:0 31px;color:#fff;font-size:17px;font-family:"Jost",sans-serif;text-decoration:none;border-right:1px solid var(--nav-line)}
.main-nav a.current{background:var(--teal);padding:0 32px}

/* hero */
.hero{position:absolute;top:182px;left:0;width:1200px;height:530px;overflow:hidden}
.hero-photo{position:absolute;inset:0;background:
  radial-gradient(ellipse 260px 200px at 560px 150px,#ffffff 0%,#f4f5f6 55%,rgba(244,245,246,0) 100%),
  radial-gradient(ellipse 170px 240px at 800px 110px,#d9dde1 0%,#c4cad0 50%,rgba(196,202,208,0) 100%),
  radial-gradient(ellipse 220px 140px at 460px 300px,#eef0f1 0%,#dfe2e4 60%,rgba(223,226,228,0) 100%),
  radial-gradient(ellipse 180px 120px at 340px 440px,#8e969d 0%,#a9b0b6 45%,rgba(169,176,182,0) 100%),
  radial-gradient(ellipse 300px 200px at 960px 360px,#fbfbfb 0%,#eceeef 60%,rgba(236,238,239,0) 100%),
  radial-gradient(ellipse 160px 300px at 1160px 180px,#c8ced3 0%,rgba(200,206,211,0) 100%),
  linear-gradient(90deg,#e4e7e9 0%,#eef0f1 12%,#dde1e4 22%,#e7e9eb 40%,#d6dbdf 65%,#e2e5e7 100%)}
.hero-photo::after{content:"";position:absolute;left:0;bottom:0;width:100%;height:160px;background:linear-gradient(180deg,rgba(226,212,196,0),rgba(214,196,176,.55))}
.hero-copy{position:absolute;left:781px;top:218px;width:305px}
.hero-copy h1{font-size:46px;font-weight:400;color:#222;line-height:1}
.hero-copy p{font-size:12.5px;line-height:22px;color:#333;margin-top:18px}
.btn{display:inline-block;color:#fff;font-size:13px;font-weight:600;text-transform:uppercase;text-decoration:none}
.hero-copy .btn{background:var(--teal);padding:11px 18px;margin-top:16px}
.arrow{position:absolute;top:227px;width:36px;height:36px;border-radius:50%;background:#333}
.arrow svg{position:absolute;left:11px;top:10px}
.arrow.prev{left:29px}.arrow.next{left:1135px}
.hero-wave{position:absolute;left:0;bottom:0}

/* treatments */
.treatments{position:absolute;top:712px;left:0;width:1200px;text-align:center}
.treatments h2{font-size:38px;margin-top:46px;line-height:1.1}
.section-intro{font-size:11.5px;line-height:21px;color:#444;width:720px;margin:16px auto 0}
.treatment-list{position:relative;height:360px}
.treatment{position:absolute;top:30px;width:230px;text-align:center}
.treatment .photo{width:194px;height:194px;border-radius:50%;margin:0 auto;border:3px solid var(--teal-light);position:relative}
.treatment .badge{position:absolute;left:76px;bottom:-20px;width:36px;height:36px;border-radius:50%;background:var(--teal);border:4px solid #fff}
.treatment h3{font-size:18px;margin-top:30px}
.treatment p{font-size:11px;line-height:20px;color:#555;margin-top:8px;padding:0 6px}

/* welcome */
.welcome{position:absolute;top:1300px;left:0;width:1200px;height:424px;background:var(--grey-bg);border-top:1px solid #e5e5e5;border-bottom:1px solid #e5e5e5}
.welcome-figure{position:absolute;left:141px;top:0;width:366px;height:422px;background:
  radial-gradient(ellipse 70px 40px at 195px 215px,#ffffff 0%,#f6f3f1 60%,rgba(246,243,241,0) 100%),
  radial-gradient(ellipse 95px 55px at 200px 340px,#ffffff 0%,#f5f1ee 60%,rgba(245,241,238,0) 100%),
  radial-gradient(ellipse 110px 230px at 195px 220px,var(--skin) 0%,#efd3c1 55%,rgba(239,211,193,0) 100%),
  radial-gradient(ellipse 170px 60px at 180px 90px,rgba(240,104,170,.35) 0%,rgba(240,104,170,0) 100%),
  radial-gradient(ellipse 170px 60px at 200px 260px,rgba(240,104,170,.30) 0%,rgba(240,104,170,0) 100%),
  radial-gradient(ellipse 150px 50px at 200px 390px,rgba(240,104,170,.30) 0%,rgba(240,104,170,0) 100%),
  var(--grey-bg)}
.welcome-copy{position:absolute;left:610px;top:82px;width:470px}
.welcome-copy h2{font-size:40px;line-height:1}
.welcome-copy p{font-size:11px;line-height:22px;color:#555;margin-top:20px}
.welcome-copy p+p{margin-top:12px}
.welcome-copy .btn{background:var(--magenta);padding:9px 14px;margin-top:20px;font-size:12px}

/* news */
.news{position:absolute;top:1724px;left:0;width:1200px;height:394px}
.news h2{position:absolute;left:98px;top:64px;font-size:31px;font-weight:300}
.news-nav{position:absolute;left:1075px;top:78px}
.news-item{position:absolute;top:135px;width:480px}
.news-item .photo{position:absolute;left:0;top:0;width:184px;height:184px;border-radius:50%;border:5px solid #eee}
.news-item .body{position:absolute;left:212px;top:6px;width:262px}
.news-item h3{font-size:17px;font-weight:400;color:#333;font-family:"Jost",sans-serif}
.news-item .date{font-size:11.5px;font-style:italic;color:var(--date);margin-top:14px}
.news-item p{font-size:11px;line-height:19px;color:#555;margin-top:10px}
.news-item .more{display:block;font-size:12px;color:#333;margin-top:10px;text-decoration:none}

/* before after */
.results{position:absolute;top:2118px;left:0;width:1200px;height:337px;background:var(--teal)}
.results h2{position:absolute;top:50px;width:100%;text-align:center;color:#fff;font-size:38px;font-weight:300}
.result{position:absolute;top:122px;width:239px;height:141px;border:3px solid #fff;box-shadow:0 14px 10px -10px rgba(0,0,0,.25)}

/* footer */
.site-footer{position:absolute;top:2455px;left:0;width:1200px;height:306px;background:var(--footer-bg)}
.footer-brand{position:absolute;left:98px;top:72px;display:flex;align-items:center;gap:12px}
.social{position:absolute;left:98px;top:176px;display:flex;gap:6px}
.social span{width:22px;height:22px;border:1px solid #777;border-radius:50%}
.site-footer h4{position:absolute;top:60px;font-family:"Jost",sans-serif;font-weight:400;font-size:22px;color:#333}
.quick h4{left:329px}
.quick ul{position:absolute;left:329px;top:102px;list-style:none}
.quick li{font-size:11.5px;color:#555;line-height:22px;padding-left:20px;position:relative}
.quick li::before{content:"";position:absolute;left:0;top:7px;width:8px;height:8px;border-radius:50%;background:var(--teal)}
.newsletter h4{left:537px}
.newsletter p{position:absolute;left:537px;top:102px;width:300px;font-size:11.5px;line-height:20px;color:#555}
.field{position:absolute;left:537px;width:291px;height:40px;background:#fff;font-size:11px;color:#444;padding:13px 14px}
.field.name{top:156px}.field.email{top:203px;width:195px}
.subscribe{position:absolute;left:732px;top:203px;width:96px;height:40px;background:var(--teal);color:#fff;font-size:12px;text-align:center;line-height:40px}
.contact h4{left:898px}
.contact address{position:absolute;left:898px;top:100px;font-style:normal;font-size:12.5px;line-height:21px;color:#555}
.contact .line{position:absolute;left:898px;font-size:12.5px;color:#555;display:flex;align-items:center;gap:12px}
.contact .phone{top:170px}.contact .mail{top:196px}
.copyright{position:absolute;top:2761px;left:0;width:1200px;height:56px;border-top:1px solid #ddd;text-align:center;line-height:56px;font-size:12px;color:#444;background:#fff}
</style>
</head>
<body>

<header class="site-header">
  <div class="brand">
    <span class="brand-dot"></span>
    <span class="brand-text"><span class="brand-name">Velmora</span><span class="brand-tag">Body &amp; Health</span></span>
  </div>
  <div class="search">SEARCH
    <svg width="12" height="12" viewBox="0 0 12 12"><circle cx="5" cy="5" r="3.6" fill="none" stroke="#333" stroke-width="1.6"/><line x1="7.6" y1="7.6" x2="11" y2="11" stroke="#333" stroke-width="1.8"/></svg>
  </div>
  <div class="lang">Danish | <span class="active">English</span></div>
</header>

<nav class="main-nav">
  <a class="current" href="#">Home</a>
  <a href="#">Velmora</a>
  <a href="#">Behandlinger</a>
  <a href="#">Produkter</a>
  <a href="#">Priser</a>
  <a href="#">Kontakt</a>
</nav>

<section class="hero">
  <div class="hero-photo" role="img" aria-label="White cryolipolysis machine with applicator hoses in a bright treatment room"></div>
  <div class="hero-copy">
    <h1 class="heading">Frys Fedtet Væk</h1>
    <p>The Cryolipolysis, is a treatment freezing fat and cellulit, and this treatment will be the Attraction of the clinic</p>
    <a class="btn" href="#">Read More</a>
  </div>
  <span class="arrow prev"><svg width="14" height="16" viewBox="0 0 14 16"><polyline points="10,2 4,8 10,14" fill="none" stroke="#fff" stroke-width="3"/></svg></span>
  <span class="arrow next"><svg width="14" height="16" viewBox="0 0 14 16"><polyline points="4,2 10,8 4,14" fill="none" stroke="#fff" stroke-width="3"/></svg></span>
  <svg class="hero-wave" width="1200" height="110" viewBox="0 0 1200 110">
    <path d="M0 96 C200 104 380 70 560 46 C760 20 980 30 1200 78 L1200 110 L0 110 Z" fill="#fff"/>
    <path d="M0 96 C200 104 380 70 560 46 C760 20 980 30 1200 78" fill="none" stroke="var(--teal)" stroke-width="4"/>
    <path d="M520 60 C700 30 900 26 1040 44 C1120 54 1170 70 1200 84 L1200 92 C1160 76 1100 62 1020 54 C880 42 700 48 520 60 Z" fill="var(--teal)"/>
  </svg>
</section>

<section class="treatments">
  <h2 class="heading">Behandlinger</h2>
  <p class="section-intro">Sed ut perspiciatis unde omnis iste natus error sit voluptatem accusantium doloremque laudantium, totam rem aperiam, eaque ipsa quae ab illo inventore veritatis et quasi architecto beatae vitae dicta sunt explicabo.</p>
  <div class="treatment-list">
    <article class="treatment" style="left:82px">
      <div class="photo" role="img" aria-label="Client resting beside a cryolipolysis machine" style="background:radial-gradient(ellipse 50px 70px at 60px 70px,#c9ced3,rgba(201,206,211,0)),radial-gradient(ellipse 60px 40px at 130px 90px,#e8c4ac,rgba(232,196,172,0)),radial-gradient(ellipse 90px 50px at 100px 145px,#dfe2e5,rgba(223,226,229,0)),#f2f3f4"><span class="badge"></span></div>
      <h3 class="heading">Cryolipolysis</h3>
      <p>Sed ut perspiciatis unde omnis iste natus error sit voluptatem accusantium doloremque laudantium</p>
    </article>
    <article class="treatment" style="left:340px">
      <div class="photo" role="img" aria-label="Waist and hips with contouring marks" style="background:radial-gradient(ellipse 50px 90px at 95px 85px,#ebc4a9,rgba(235,196,169,0)),radial-gradient(ellipse 55px 25px at 95px 125px,#ffffff,rgba(255,255,255,0)),radial-gradient(circle at 50% 50%,#f3e2d7,#ddefe7)"><span class="badge"></span></div>
      <h3 class="heading">Trimcurve</h3>
      <p>Sed ut perspiciatis unde omnis iste natus error sit voluptatem accusantium doloremque laudantium</p>
    </article>
    <article class="treatment" style="left:596px">
      <div class="photo" role="img" aria-label="Relaxing massage by candlelight" style="background:radial-gradient(ellipse 40px 30px at 50px 60px,#fff1c8,rgba(255,241,200,0)),radial-gradient(ellipse 40px 30px at 145px 55px,#ffe6b0,rgba(255,230,176,0)),radial-gradient(ellipse 80px 45px at 110px 120px,#e3ad8a,rgba(227,173,138,0)),linear-gradient(180deg,#a8733f,#5e3a22)"><span class="badge"></span></div>
      <h3 class="heading">Lymfemassage</h3>
      <p>Sed ut perspiciatis unde omnis iste natus error sit voluptatem accusantium doloremque laudantium</p>
    </article>
    <article class="treatment" style="left:864px">
      <div class="photo" role="img" aria-label="Therapist in blue gloves applying a treatment device" style="background:radial-gradient(ellipse 45px 35px at 135px 55px,var(--glove),rgba(91,111,184,0)),radial-gradient(ellipse 40px 30px at 150px 130px,#2f5f96,rgba(47,95,150,0)),radial-gradient(ellipse 80px 50px at 80px 115px,#e7c2aa,rgba(231,194,170,0)),linear-gradient(135deg,#c9d7e6,#f1e7e1)"><span class="badge"></span></div>
      <h3 class="heading">Produkter</h3>
      <p>Sed ut perspiciatis unde omnis iste natus error sit voluptatem accusantium doloremque laudantium</p>
    </article>
  </div>
</section>

<section class="welcome">
  <div class="welcome-figure" role="img" aria-label="Slim woman in white underwear wrapped by a pink ribbon"></div>
  <div class="welcome-copy">
    <h2 class="heading">Welcome To Velmora</h2>
    <p>Sed ut perspiciatis unde omnis iste natus error sit voluptatem accusantium doloremque laudantium, totam rem aperiam, eaque ipsa quae ab illo inventore veritatis et quasi architecto beatae vitae dicta sunt explicabo. Nemo enim ipsam voluptatem quia voluptas sit aspernatur</p>
    <p>Sed ut perspiciatis unde omnis iste natus error sit voluptatem accusantium doloremque laudantium, totam rem aperiam</p>
    <a class="btn" href="#">Read More</a>
  </div>
</section>

<section class="news">
  <h2 class="heading">Latest News</h2>
  <svg class="news-nav" width="26" height="14" viewBox="0 0 26 14"><polyline points="7,2 2,7 7,12" fill="none" stroke="#333" stroke-width="2"/><polyline points="19,2 24,7 19,12" fill="none" stroke="#333" stroke-width="2"/></svg>
  <article class="news-item" style="left:100px">
    <div class="photo" role="img" aria-label="Treatment device applied to a client's back" style="background:radial-gradient(ellipse 40px 30px at 120px 40px,var(--glove),rgba(91,111,184,0)),radial-gradient(ellipse 45px 40px at 55px 80px,#1f4f86,rgba(31,79,134,0)),radial-gradient(ellipse 90px 50px at 95px 130px,#ecd0bd,rgba(236,208,189,0)),linear-gradient(160deg,#d6dee8,#f3ebe6)"></div>
    <div class="body">
      <h3>Nulla at diam ornare, aliquam urna</h3>
      <div class="date">JAN 25, 2017</div>
      <p>Nulla at diam ornare, aliquam urna vel, commodo urna. Nam id risus a est luctus consectetur quis eget libero. Suspendisse potenti. Pellentesque habitant morbi tristique senectus</p>
      <a class="more" href="#">Read More +</a>
    </div>
  </article>
  <article class="news-item" style="left:633px">
    <div class="photo" role="img" aria-label="Woman measuring her waist" style="background:radial-gradient(ellipse 50px 35px at 85px 45px,#ffffff,rgba(255,255,255,0)),radial-gradient(ellipse 65px 60px at 90px 110px,#eccdb8,rgba(236,205,184,0)),radial-gradient(ellipse 20px 18px at 70px 110px,#f0a640,rgba(240,166,64,0)),linear-gradient(180deg,#eef1f4,#f6efea)"></div>
    <div class="body">
      <h3>Nulla at diam ornare, aliquam urna</h3>
      <div class="date">JAN 25, 2017</div>
      <p>Nulla at diam ornare, aliquam urna vel, commodo urna. Nam id risus a est luctus consectetur quis eget libero. Suspendisse potenti. Pellentesque habitant morbi tristique senectus</p>
      <a class="more" href="#">Read More +</a>
    </div>
  </article>
</section>

<section class="results">
  <h2 class="heading">før efter</h2>
  <div class="result" style="left:100px;background:radial-gradient(ellipse 50px 60px at 60px 80px,#c98e6c,rgba(201,142,108,0)),radial-gradient(ellipse 45px 60px at 175px 80px,#d8a98c,rgba(216,169,140,0)),radial-gradient(ellipse 30px 14px at 175px 70px,#6e7a99,rgba(110,122,153,0)),linear-gradient(90deg,#7c8a6a,#a8b0b8 50%,#cfc9c4)" role="img" aria-label="Before and after body contouring, swimwear"></div>
  <div class="result" style="left:355px;background:radial-gradient(ellipse 35px 60px at 65px 75px,#e3b89c,rgba(227,184,156,0)),radial-gradient(ellipse 30px 60px at 170px 75px,#e6bfa6,rgba(230,191,166,0)),radial-gradient(ellipse 40px 22px at 65px 55px,#fff,rgba(255,255,255,0)),radial-gradient(ellipse 36px 22px at 170px 55px,#fff,rgba(255,255,255,0)),linear-gradient(90deg,#d9d9d9,#ececec 50%,#d9d9d9)" role="img" aria-label="Before and after side profile"></div>
  <div class="result" style="left:610px;background:radial-gradient(ellipse 55px 40px at 60px 40px,#2a2526,rgba(42,37,38,0)),radial-gradient(ellipse 55px 40px at 180px 40px,#2a2526,rgba(42,37,38,0)),radial-gradient(ellipse 60px 45px at 60px 100px,#d2a185,rgba(210,161,133,0)),radial-gradient(ellipse 50px 45px at 180px 100px,#dbb094,rgba(219,176,148,0)),linear-gradient(180deg,#e9e6e4,#cfc8c4)" role="img" aria-label="Before and after waist reduction"></div>
  <div class="result" style="left:864px;background:radial-gradient(ellipse 45px 65px at 60px 70px,#ddb295,rgba(221,178,149,0)),radial-gradient(ellipse 45px 65px at 175px 70px,#e4bca0,rgba(228,188,160,0)),radial-gradient(ellipse 30px 12px at 60px 100px,#2a2526,rgba(42,37,38,0)),radial-gradient(ellipse 28px 12px at 175px 100px,#2a2526,rgba(42,37,38,0)),linear-gradient(90deg,#f5f2f0,#fbfaf9 50%,#f5f2f0)" role="img" aria-label="Before and after buttocks treatment"></div>
</section>

<footer class="site-footer">
  <div class="footer-brand">
    <span class="brand-dot"></span>
    <span class="brand-text"><span class="brand-name" style="font-size:40px">Velmora</span><span class="brand-tag">Body &amp; Health</span></span>
  </div>
  <div class="social"><span></span><span></span><span></span><span></span><span></span></div>

  <div class="quick">
    <h4>Quick Links</h4>
    <ul><li>Home</li><li>Velmora</li><li>Behandlinger</li><li>Produkter</li><li>Priser</li><li>Blog</li><li>Kontakt</li></ul>
  </div>

  <div class="newsletter">
    <h4>Sign up for Newsletter</h4>
    <p>Sed ut perspiciatis unde omnis iste natus error sit voluptatem accusantium doloremque</p>
    <div class="field name">Enter Name</div>
    <div class="field email">Enter Email</div>
    <div class="subscribe">SUBSCRIBE</div>
  </div>

  <div class="contact">
    <h4>Contact Us</h4>
    <address>Velmora<br>12 Elm Row&nbsp; Harbourton<br>PA 17400</address>
    <div class="line phone"><svg width="16" height="16" viewBox="0 0 16 16"><path d="M3 1 L6 1 L7 5 L5 6.5 C6 9 7 10 9.5 11 L11 9 L15 10 L15 13 C15 14 14 15 13 15 C6 15 1 10 1 3 C1 2 2 1 3 1 Z" fill="none" stroke="var(--green-link)" stroke-width="1.4"/></svg>Phone : 555-0142-7781</div>
    <div class="line mail"><svg width="16" height="12" viewBox="0 0 16 12"><rect x="1" y="1" width="14" height="10" fill="none" stroke="var(--green-link)" stroke-width="1.4"/><polyline points="1,1 8,7 15,1" fill="none" stroke="var(--green-link)" stroke-width="1.4"/></svg>Email : info@velmora.example</div>
  </div>
</footer>

<div class="copyright">©2017 Velmora .. All Rights Reserved.</div>

</body>
</html>
```